KestrelNet Business Cards

Create business cards for our exciting new software company. We provide cloud billing systems and provisioning software for campany that need monthly SaaS and Cloud Billing

Target Market(s)

Enterprise businesses, b2b, telecom carriers, software manufactures

Industry/Entity Type

Software

```html
<!DOCTYPE html>
<html lang="en">
<head>
<meta charset="utf-8">
<title>KestrelNet Business Cards</title>
<link rel="stylesheet" href="https://fonts.googleapis.com/css2?family=Questrial&family=Arimo:wght@400;700&display=swap">
<style>
  :root {
    --backdrop: #e4e6ea;
    --card-white: #ffffff;
    --navy: #1f3657;
    --navy-light: #2f4d72;
    --brand-blue: #5aa6d3;
    --brand-deep: #2c5d8c;
    --ink: #1e2f4d;
    --ink-soft: #5a6b84;
  }
  * { box-sizing: border-box; margin: 0; padding: 0; }
  html, body {
    width: 1200px;
    height: 800px;
    overflow: hidden;
    background: var(--backdrop);
  }
  .sheet {
    position: relative;
    width: 1200px;
    height: 800px;
    display: flex;
    align-items: center;
    justify-content: center;
    gap: 40px;
  }
  .card {
    position: relative;
    width: 540px;
    height: 309px;
    border-radius: 3px;
    box-shadow: 0 6px 18px rgba(20, 35, 60, 0.18);
    overflow: hidden;
  }
  .card--front { background: var(--card-white); }
  .card--back {
    background: linear-gradient(135deg, var(--navy) 0%, var(--navy) 55%, var(--navy-light) 100%);
  }

  .brand {
    display: flex;
    align-items: center;
    gap: 8px;
  }
  .brand__dot {
    width: 14px;
    height: 14px;
    border-radius: 50%;
    background: var(--brand-blue);
  }
  .brand__name {
    font-family: "Questrial", sans-serif;
    font-size: 30px;
    line-height: 1;
    color: var(--brand-deep);
  }
  .brand__tagline {
    font-family: "Arimo", sans-serif;
    font-size: 7px;
    letter-spacing: 1.2px;
    text-transform: uppercase;
    color: var(--ink-soft);
    line-height: 1.3;
    margin-top: 4px;
    text-align: right;
  }

  /* Front */
  .front__identity {
    position: absolute;
    right: 34px;
    top: 36px;
    display: flex;
    flex-direction: column;
    align-items: flex-end;
  }
  .front__person {
    position: absolute;
    right: 34px;
    top: 128px;
    text-align: right;
    font-family: "Arimo", sans-serif;
    color: var(--ink);
  }
  .person__name {
    font-size: 15px;
    letter-spacing: 0.5px;
    text-transform: uppercase;
  }
  .person__title {
    font-size: 9px;
    color: var(--ink-soft);
    letter-spacing: 0.5px;
  }
  .front__contact {
    position: absolute;
    right: 34px;
    bottom: 36px;
    text-align: right;
    font-family: "Arimo", sans-serif;
    font-size: 13px;
    line-height: 1.35;
    color: var(--ink);
  }
  .contact__label { color: var(--ink-soft); }

  /* Back */
  .back__identity {
    position: absolute;
    left: 64px;
    top: 112px;
  }
  .card--back .brand__name {
    color: var(--brand-blue);
    font-size: 40px;
  }
  .card--back .brand__dot { width: 18px; height: 18px; }
  .card--back .brand__tagline {
    color: #c9d8ea;
    font-size: 8px;
  }
  .back__url {
    position: absolute;
    left: 64px;
    bottom: 58px;
    font-family: "Arimo", sans-serif;
    font-size: 12px;
    letter-spacing: 5px;
    color: #d7e3f1;
  }
</style>
</head>
<body>
<main class="sheet">
  <section class="card card--front" aria-label="Business card front">
    <div class="front__identity">
      <div class="brand">
        <span class="brand__dot"></span>
        <span class="brand__name">KestrelNet</span>
      </div>
      <p class="brand__tagline">Cloud billing and<br>operational support systems</p>
    </div>
    <div class="front__person">
      <p class="person__name">Marcus Hale</p>
      <p class="person__title">CEO</p>
    </div>
    <address class="front__contact" style="font-style: normal;">
      <p>KestrelNet</p>
      <p>4470 Harbor Point Rd, Easton, MD 21601</p>
      <p><span class="contact__label">P:</span> 555.014.2200 x 2204 <span class="contact__label">F:</span> 555.014.2201</p>
      <p>www.KESTRELNET.com</p>
    </address>
  </section>

  <section class="card card--back" aria-label="Business card back">
    <div class="back__identity">
      <div class="brand">
        <span class="brand__dot"></span>
        <span class="brand__name">KestrelNet</span>
      </div>
      <p class="brand__tagline">Cloud billing and<br>operational support systems</p>
    </div>
    <p class="back__url">www.KestrelNet.com</p>
  </section>
</main>
</body>
</html>
```